Redesign trade show stand graphics for Harbour Panelworks

Update existing graphics of a trade show stand consisting of 2 walls. See the current design attached.

Left wall size is 2.4m high x 2700mm wide (made up of 3 pieces of 2400mm high x 900mm wide). The artwork will be printed on self adhesive stickers to cover the 2 walls.

NEW DESIGN LEFT WALL (2.4m high x 3m wide)
Headline at the top of the wall should read:
RENOVATE YOUR KITCHEN
the quick, easy and cost effective way:
JUST REPLACE THE DOORS and panels
• Cost effective: Save $$$
• Quick: approx. 15 working days
• Easy: No mess or inconvenience
• Polyurethane finish, unlimited choice of colours
• Measure, quote and install - DIY or contact our installers
• Delivery Australia wide
Harbour Panelworks logo at top of left and right walls. See logo attached. “Trueborn Goods” logo somewhere on the wall (logo attached)
The main body of the left wall will contain a “before” and “after” photo of a kitchen. Size of “before” shot approximately 250mm wide x 150mm high and “after” shot approximately 1m wide x 600mm high. Photo with higher resolution will be supplied.
Text:
• We replace doors, panels, drawer fronts and kickboards - all painted in polyurethane.
• We drill doors for new or existing hinges. We supply Kelto soft closing hinges, door handles, wardrobe door tracks and decorative items such as corbels, flutes and rosettes and capping.
• Our installers measure, quote and install or save money and do it yourself - DIY
Headline under the above: UPDATE YOUR BUILT IN WARDROBES WITH NEW DOORS
Sub headline: Custom made to your sizes and painted in polyurethane in the colour of your choice
2 photos of wardrobes to go under this headline

NEW DESIGN RIGHT WALL (2.4m high x 2800mm wide made up of 1 x 1000mm piece and 2 x 900mm pieces)
Visit our website: harbourpanelworks.com.au
Headline: SAVE TIME AND MONEY – REPLACE YOUR OLD DOORS (and panels)
Sub headline: WITH ONES PAINTED IN POLYURETHANE
Sub sub headline:
TO GET A QUOTE:
• DIY measure doors and panels and fill in our Quote Form or
• Contact our installers to measure, quote and install

At 1.5m high: 2 rows of 7 rectangular outlines 400mm high x 300mm wide (for sample doors that will be hung on the wall).
Directly under that, another headline:
Many more designs in our showroom at
47 Marlowe Avenue, Brindale Heights NSW 2871
Phone: (02) 9318 0627
Email: sales@harbourpanelworks.com.au
Website: harbourpanelworks.com.au
Place image of our showroom (attached) to the left or right.

“Trueborn Goods” logo and "Open Bench Club" logo somewhere on the wall (logos attached).
Small listing of approximately A5 size of “What we do”, “What we don’t do” and “What you do”. These will be supplied in bullet points.
Another image to use is uploaded below.

Target Market(s)

Home owners, home renovators

Industry/Entity Type

Trade

Font styles to use
Sans Serif
Other font styles liked:
• A font similar to that used on our website www.harbourpanelworks.com.au

Colors
f8972e

Requirements
Must have
• The background colour of the stand artwork should remain the same bright colour of our logo. The fonts should be similar to that used on our website www.harbourpanelworks.com.au
Nice to have
• Fun and engaging design

```html
<!DOCTYPE html>
<html lang="en">
<head>
<meta charset="utf-8">
<title>Harbour Panelworks – Stand Wall</title>
<link href="https://fonts.googleapis.com/css2?family=Bebas+Neue&family=Open+Sans:wght@400;600;700;800&display=swap" rel="stylesheet">
<style>
  :root {
    --page: #8a8a8a;
    --brand-yellow: #f9bb59;
    --charcoal: #3e3e3e;
    --ink: #3a3a3a;
    --outline: #5a5a5a;
    --web-yellow: #f9c25a;
    --orange: #f47b20;
    --red: #d9252a;
    --white: #ffffff;
    --grey-text: #5a5a5a;
  }
  * { box-sizing: border-box; margin: 0; padding: 0; }
  html, body { width: 1200px; height: 1034px; overflow: hidden; background: var(--page); }
  body { position: relative; font-family: "Open Sans", Arial, sans-serif; }

  .wall {
    position: absolute; left: 20px; top: 51px;
    width: 1016px; height: 816px;
    transform: scale(1.1417); transform-origin: 0 0;
    background: var(--white); overflow: hidden;
  }
  .band-top { position: absolute; left: 0; top: 0; width: 1016px; height: 172px; background: var(--brand-yellow); }
  .band-dark { position: absolute; left: 0; top: 172px; width: 1016px; height: 323px; background: var(--charcoal); }
  .band-quote { position: absolute; left: 0; top: 495px; width: 1016px; height: 178px; background: var(--brand-yellow); }

  .headline {
    position: absolute; left: 0; top: 42px; width: 956px; text-align: center;
    font-family: "Bebas Neue", Impact, sans-serif; font-size: 53px; line-height: 56px;
    color: var(--ink); letter-spacing: 0.5px; white-space: nowrap;
  }
  .subheadline {
    position: absolute; left: 0; top: 96px; width: 940px; text-align: center;
    font-weight: 800; font-size: 17px; color: var(--white); letter-spacing: 0.5px; white-space: nowrap;
  }
  .brand-mark {
    position: absolute; left: 916px; top: 20px; width: 92px;
    display: flex; flex-direction: column; align-items: center; gap: 6px;
  }
  .brand-mark .square { width: 22px; height: 22px; background: var(--ink); }
  .brand-mark .name {
    font-weight: 800; font-size: 14px; line-height: 16px; color: var(--ink); text-align: center;
  }

  .sample-slots { position: absolute; left: 96px; top: 142px; }
  .slot {
    position: absolute; width: 106px; height: 140px;
    border: 1.5px solid var(--outline); opacity: 0.4;
  }

  .website {
    position: absolute; left: 0; top: 444px; width: 1016px; text-align: center;
    font-weight: 700; font-size: 27px; color: var(--web-yellow); white-space: nowrap;
  }

  .showroom-frame {
    position: absolute; left: 46px; top: 516px; width: 448px; height: 273px;
    background: var(--white); box-shadow: 0 18px 14px -12px rgba(0,0,0,0.35);
  }
  .showroom-photo {
    position: absolute; left: 10px; top: 10px; width: 428px; height: 253px;
    background: linear-gradient(180deg, #e9e9e4 0%, #d8d6cf 55%, #6f7479 62%, #5d6166 100%);
  }

  .quote-ribbon { position: absolute; left: 513px; top: 515px; width: 390px; height: 26px; }
  .quote-ribbon svg { position: absolute; left: 0; top: 0; }
  .quote-ribbon span {
    position: absolute; left: 10px; top: 3px;
    font-weight: 700; font-size: 15px; color: var(--white); white-space: nowrap;
  }

  .step { position: absolute; display: flex; align-items: flex-start; }
  .step svg { flex: none; margin-right: 4px; }
  .step .num { font-weight: 800; font-size: 21px; color: var(--red); line-height: 22px; margin-right: 5px; }
  .step p { font-weight: 700; font-size: 11px; line-height: 13.5px; color: var(--ink); white-space: nowrap; }

  .contact { position: absolute; left: 486px; top: 698px; width: 400px; text-align: center; }
  .contact .showroom { font-weight: 800; font-size: 21px; color: var(--grey-text); white-space: nowrap; }
  .contact .address { font-size: 13.5px; color: var(--ink); margin-top: 2px; }
  .contact .phone { font-weight: 800; font-size: 24px; color: var(--orange); margin-top: 4px; }
  .contact .email { font-size: 13px; color: var(--ink); }

  .open-bench {
    position: absolute; left: 868px; top: 700px; width: 92px; height: 92px; border-radius: 50%;
    background: var(--orange); color: var(--white);
    display: flex; align-items: center; justify-content: center; text-align: center;
    font-family: "Bebas Neue", Impact, sans-serif; font-size: 19px; line-height: 19px;
  }
</style>
</head>
<body>
  <main class="wall">
    <div class="band-top"></div>
    <div class="band-dark"></div>
    <div class="band-quote"></div>

    <h1 class="headline">Save time and money - replace your old doors</h1>
    <p class="subheadline">AND PANELS WITH NEW CUSTOM MADE ONES PAINTED IN POLYURETHANE FINISH</p>

    <div class="brand-mark">
      <div class="square"></div>
      <div class="name">Harbour Panelworks</div>
    </div>

    <div class="sample-slots">
      <div class="slot" style="left:0;top:0"></div>
      <div class="slot" style="left:118px;top:0"></div>
      <div class="slot" style="left:236px;top:0"></div>
      <div class="slot" style="left:354px;top:0"></div>
      <div class="slot" style="left:472px;top:0"></div>
      <div class="slot" style="left:590px;top:0"></div>
      <div class="slot" style="left:708px;top:0"></div>
      <div class="slot" style="left:0;top:152px"></div>
      <div class="slot" style="left:118px;top:152px"></div>
      <div class="slot" style="left:236px;top:152px"></div>
      <div class="slot" style="left:354px;top:152px"></div>
      <div class="slot" style="left:472px;top:152px"></div>
      <div class="slot" style="left:590px;top:152px"></div>
      <div class="slot" style="left:708px;top:152px"></div>
    </div>

    <p class="website">Visit our website: harbourpanelworks.com.au</p>

    <div class="showroom-frame">
      <div class="showroom-photo" role="img" aria-label="Showroom interior with white sliding wardrobe doors and a curved wall of sample door panels"></div>
    </div>

    <div class="quote-ribbon">
      <svg width="390" height="26" viewBox="0 0 390 26"><polygon points="0,0 390,0 378,13 390,26 0,26" fill="var(--red)"/></svg>
      <span>HOW TO GET A QUOTE OR PLACE AN ORDER</span>
    </div>

    <div class="step" style="left:520px;top:550px">
      <svg width="40" height="38" viewBox="0 0 42 40" fill="none" stroke="var(--ink)" stroke-width="2.5">
        <rect x="4" y="14" width="32" height="10" transform="rotate(40 20 19)"/>
        <path d="M8 34 L30 6 L35 10 L13 38 L6 39 Z"/>
      </svg>
      <span class="num">01</span>
      <p>Choose your door<br>design, edges, colour,<br>finish and accessories.</p>
    </div>

    <div class="step" style="left:512px;top:608px">
      <svg width="48" height="32" viewBox="0 0 50 34" fill="none" stroke="var(--ink)" stroke-width="2.5">
        <line x1="2" y1="12" x2="12" y2="12"/><line x1="0" y1="19" x2="12" y2="19"/><line x1="4" y1="26" x2="14" y2="26"/>
        <rect x="16" y="6" width="32" height="22" fill="var(--ink)"/>
        <polyline points="16,6 32,19 48,6" stroke="var(--brand-yellow)"/>
      </svg>
      <span class="num">02</span>
      <p>DIY or get an installer<br>to measure your<br>doors and panels and fill in<br>a quote form.</p>
    </div>

    <div class="step" style="left:752px;top:550px">
      <svg width="44" height="44" viewBox="0 0 46 46">
        <circle cx="18" cy="18" r="15" fill="var(--ink)"/>
        <text x="18" y="25" text-anchor="middle" font-family="Open Sans, sans-serif" font-weight="800" font-size="19" fill="var(--brand-yellow)">$</text>
        <path d="M26 30 L40 26 L44 40 L30 44 Z" fill="var(--ink)"/>
      </svg>
      <span class="num">03</span>
      <p>On receipt of our quote,<br>pay 50% deposit to order<br>your doors. If using an installer,<br>they will quote the installation.</p>
    </div>

    <div class="step" style="left:756px;top:618px">
      <svg width="42" height="28" viewBox="0 0 44 30" fill="var(--ink)">
        <rect x="0" y="2" width="26" height="20"/>
        <path d="M28 8 H37 L43 15 V22 H28 Z"/>
        <circle cx="9" cy="25" r="4"/><circle cx="35" cy="25" r="4"/>
      </svg>
      <span class="num">04</span>
      <p>Your doors will be ready<br>for delivery or pick up in<br>approx. 15 working days.</p>
    </div>

    <div class="contact">
      <p class="showroom">More designs in our showroom</p>
      <p class="address">47 Marlowe Avenue, Brindale Heights NSW 2871</p>
      <p class="phone">Phone: (02) 9318 0627</p>
      <p class="email">Email: sales@harbourpanelworks.com.au</p>
    </div>

    <div class="open-bench">OPEN<br>BENCH<br>CLUB</div>
  </main>
</body>
</html>
```